Elegant Business Card for Technology Company

Client is a supplier of innovative industrial communications and automation equipment since 2002. This contest is to gather fresh ideas for a redesign of the existing business card. Client is looking for design that best communicates tagline "Industrial Networking and Computing Specialist".

Design submissions should look modern, clean, elegant and professional. It should not be cluttered. Use white as the primary colour. Orange and black as secondary colour. Refer to jpeg File 1 on the current design.

Fonts used by Client used include Arial Regular, Arial Black, Roboto Regular, Roboto Black and Lato.

The winning design will be sent for offset printing using super white 250gsm artcard paper (open for suggestions).

Target Market(s)

System Engineers, Project Managers, Purchasing Managers from companies providing engineering services for Smart Cities.

Industry/Entity Type

Information Technology

Contact Information for Business Card

Refer to PDF File 3 for Business Card Details. Priority of short contact information would be as follows Name > Job Title > Email > Mobile > Web > Tel > Fax > Business Address >UEN (UEN represents company registration number)

Font styles to use
Sans Serif

Colors
ffffff
f37122
000000
5c5c5c

Requirements
Must have
• Refer to AI File 2 (Company Logo) & PDF File 3 (Information on Namecard)
Should not have
• No QR codes
• No Social Media Icons
• Do not create full Black or Orange colour background

```html
<!DOCTYPE html>
<html lang="en">
<head>
<meta charset="utf-8">
<title>Korvex Asia Pacific – Business Card</title>
<link rel="stylesheet" href="https://fonts.googleapis.com/css2?family=Roboto:wght@400;500;700&display=swap">
<style>
  :root {
    --white: #ffffff;
    --orange: #f37122;
    --orange-deep: #d9601a;
    --black: #000000;
    --ink: #1e1e1e;
    --grey: #5c5c5c;
    --grey-soft: #c9c9c9;
    --stage: #e4e4e4;
  }
  * { box-sizing: border-box; margin: 0; padding: 0; }
  html, body { width: 1200px; height: 900px; overflow: hidden; }
  body {
    background: var(--stage);
    font-family: "Roboto", Arial, sans-serif;
    color: var(--ink);
    position: relative;
  }
  .card {
    position: absolute;
    width: 580px;
    height: 330px;
    background: linear-gradient(135deg, var(--white) 45%, #ededed 100%);
    box-shadow: 0 6px 18px rgba(0,0,0,.18);
    overflow: hidden;
  }
  .card--front { left: 70px; top: 100px; }
  .card--back { left: 550px; top: 470px; }

  /* brand */
  .brand { position: absolute; display: flex; align-items: center; gap: 12px; }
  .brand__dot { width: 46px; height: 46px; border-radius: 50%; background: var(--orange); }
  .brand__name { font-weight: 700; font-size: 40px; letter-spacing: 1px; color: var(--ink); line-height: 1; }
  .company { position: absolute; left: 98px; top: 94px; font-weight: 700; font-size: 14px; color: var(--ink); }

  .decor {
    position: absolute; top: 0; right: 0; width: 190px; height: 215px;
    border-radius: 0 0 0 90px;
  }
  .card--front .decor { background: linear-gradient(160deg, var(--orange) 0%, var(--orange-deep) 100%); opacity: .9; }
  .card--back .decor { background: linear-gradient(160deg, #d8d8d8 0%, #f0f0f0 100%); height: 330px; border-radius: 120px 0 0 120px; width: 170px; }

  /* front */
  .card--front .brand { left: 40px; top: 42px; }
  .person { position: absolute; left: 40px; top: 222px; display: flex; align-items: baseline; gap: 14px; }
  .person__name { font-weight: 700; font-size: 21px; color: var(--ink); }
  .person__role { font-size: 14px; color: var(--grey); border-left: 1px solid var(--grey); padding-left: 14px; }
  .address-band {
    position: absolute; left: 0; top: 256px; width: 100%; height: 28px;
    background: var(--black); color: var(--orange);
    font-size: 13px; padding: 6px 40px; white-space: nowrap;
  }
  .contact-band {
    position: absolute; left: 0; top: 284px; width: 100%; height: 46px;
    background: var(--orange); padding: 6px 40px;
    display: grid; grid-template-columns: 170px 180px 1fr; row-gap: 2px;
    font-size: 12px; color: var(--white);
  }
  .contact-band b { color: var(--ink); font-weight: 700; display: inline-block; width: 22px; }
  .contact-band .uen b { width: auto; margin-right: 6px; }

  /* back */
  .card--back .brand { left: 44px; top: 112px; }
  .rule { position: absolute; left: 150px; top: 176px; width: 430px; height: 3px; background: var(--orange); }
  .tagline { position: absolute; left: 150px; top: 186px; font-size: 14px; color: var(--ink); letter-spacing: .3px; }
  .services {
    position: absolute; right: 44px; top: 34px; list-style: none;
    text-align: right; font-size: 14px; line-height: 21px; color: var(--ink);
  }
  .services li::after {
    content: ""; display: inline-block; width: 5px; height: 5px; border-radius: 50%;
    background: var(--orange); margin-left: 8px; vertical-align: middle;
  }
  .services li:first-child::after { background: transparent; }
</style>
</head>
<body>
  <article class="card card--front">
    <div class="decor" role="img" aria-label="Decorative orange dot-grid brand motif"></div>
    <div class="brand"><span class="brand__dot"></span><span class="brand__name">KORVEX</span></div>
    <p class="company">Korvex Asia Pacific Pte Ltd</p>
    <div class="person">
      <span class="person__name">Daniel Lim</span>
      <span class="person__role">Sales Manager</span>
    </div>
    <p class="address-band">22 Harbour Link Business Hub #05-12 (Lobby B), Singapore 418720</p>
    <div class="contact-band">
      <span><b>M.</b> +65 9123 4567</span>
      <span><b>T.</b> +65 6321 4580</span>
      <span><b>F.</b> +65 6321 4581</span>
      <span><b>E.</b> sales@korvex.com.sg</span>
      <span><b>W.</b> www.korvex.com.sg</span>
      <span class="uen"><b>UEN No</b>200507341K</span>
    </div>
  </article>

  <article class="card card--back">
    <div class="decor" role="img" aria-label="Faint grey dot-grid brand motif"></div>
    <ul class="services">
      <li>Industrial Ethernet / Wireless / Cellular</li>
      <li>Industrial and Embedded Computing</li>
      <li>Serial / Fieldbus Connectivity</li>
      <li>IP Video Surveillance</li>
      <li>Remote Automation</li>
    </ul>
    <div class="brand"><span class="brand__dot"></span><span class="brand__name">KORVEX</span></div>
    <div class="rule"></div>
    <p class="tagline">Industrial Networking and Computing Specialist</p>
  </article>
</body>
</html>
```